Taro Velmund Website

I have a client who is a physical therapist who I am redeveloping a website for. The new site will be a combination of two sites, once that handles the practice site of the business and another for the education side of the business in which they will accept online registration for therapeutic training courses for physical therapy students.

The existing sites (just for background purposes) are here:

Private Practice: http://brivantelinc.com/
Education: http://doltrafoundation.com/

So, the new site will be a modern looking site that combines both the private practice content and the education content (register for classes) information.

The home page should have a clear distinction between private practice and education. I am thinking that a button or icon to view/register for classes somewhere on the Home page would lead users to that section of the website that deals specifically with education.

So, that said, I am think the navigation should include the following:

Home
About Us
Our Services
Education
Contact Us

The client has provided the following websites as examples sites in which they like the colors. Here is the direct quote from the client:

"We were looking for sites that looked comfortable in colors and presentation, please view so you have a better idea what we want the feel and colors to be like

http://www.pikowestrips.com/

http://www.marnefield.com/

www.zelquabeam.com"

Note that all examples they provided have a similar type of layout with a large slideshow image front and center, horizontal navigation and large footer areas with contact information and links to pages and social networks.

I am also going to be working on a logo for them, I have yet to decide on what text that will include or what icons (if any) will be a part of that. I am thinking that the doctor's name "Taro Velmund" but I am still struggling with that so a placeholder logo for now would be fine.

```html
<!DOCTYPE html>
<html lang="en">
<head>
<meta charset="utf-8">
<title>Taro Velmund – Physical Therapy &amp; Education</title>
<link href="https://fonts.googleapis.com/css2?family=Cabin:wght@400;600;700&family=Open+Sans:ital,wght@0,400;0,600;0,700;1,400&display=swap" rel="stylesheet">
<style>
:root{
  --cyan:#1aa6d6;
  --ink:#444;
  --muted:#777;
  --light:#efefef;
  --tan:#d6b66a;
  --tan-btn:#b98a2e;
  --green:#a9c46a;
  --green-btn:#6f9a2c;
  --navy:#2f2b52;
  --orange:#e08a1e;
  --teal:#1e5561;
  --magenta:#b0186e;
  --dark:#3b3b3b;
  --white:#fff;
}
*{box-sizing:border-box;margin:0;padding:0}
html,body{width:1200px;height:3913px;overflow:hidden}
body{font-family:"Open Sans",Arial,sans-serif;color:var(--ink);background:var(--white)}
h1,h2,h3,h4{font-family:"Cabin","Open Sans",sans-serif}
.section-title{font-size:40px;font-weight:600;color:var(--cyan);text-align:center}
.section-sub{font-style:italic;font-size:17px;color:var(--muted);text-align:center;margin-top:10px}
.divider{width:260px;height:1px;background:#ccc;margin:22px auto;position:relative}
.divider::after{content:"";position:absolute;left:50%;top:-4px;width:8px;height:8px;margin-left:-4px;border-radius:50%;background:#bbb}
.btn{display:inline-block;font-family:"Open Sans",sans-serif;font-weight:700;font-size:15px;text-transform:uppercase;padding:14px 26px;border-radius:3px;color:var(--white)}

/* header */
.site-header{height:98px;display:flex;align-items:center;padding:0 137px 0 137px;justify-content:space-between}
.brand{font-family:"Cabin",sans-serif;font-size:32px;font-weight:600;color:var(--cyan)}
.main-nav{display:flex;align-items:center;gap:30px;font-size:15px;font-weight:600;color:#333}
.main-nav .active{color:var(--cyan)}
.account{display:flex;gap:6px;margin-left:10px}
.account span{font-size:12px;color:var(--white);padding:4px 10px;border-radius:2px}
.account .login{background:var(--cyan)}
.account .register{background:#888}

/* hero */
.hero{position:relative;height:597px;background:linear-gradient(120deg,#e7ddd2 0%,#d9c6b3 40%,#c79a6c 70%,#efe6da 100%)}
.hero-caption{position:absolute;left:277px;top:330px;color:var(--white);text-shadow:0 1px 4px rgba(0,0,0,.5)}
.hero-caption h1{font-size:38px;font-weight:700}
.hero-caption p{font-size:19px;line-height:1.4;width:380px;margin-top:6px}
.hero-arrow{position:absolute;top:345px;width:52px;height:52px;border-radius:50%;background:rgba(255,255,255,.55)}
.hero-arrow.prev{left:48px}.hero-arrow.next{right:48px}
.hero-arrow svg{width:52px;height:52px}

/* about */
.about{height:315px;padding-top:62px;text-align:center}
.about p{width:820px;margin:0 auto;font-size:16px;line-height:1.7;color:var(--muted)}

/* split */
.split{display:flex;height:310px}
.split-panel{flex:1;text-align:center;color:var(--white);padding-top:44px}
.split-panel h3{font-size:30px;font-weight:600}
.split-panel p{width:440px;margin:18px auto 26px;font-size:13px;line-height:1.6;opacity:.9}
.practice{background:var(--tan)}.practice .btn{background:var(--tan-btn)}
.education{background:var(--green)}.education .btn{background:var(--green-btn)}

/* classes */
.next-class{background:var(--light);height:750px;padding-top:68px}
.next-date{text-align:center;color:var(--orange);font-size:17px;margin-top:-6px}
.class-grid{display:grid;grid-template-columns:1fr 1fr;width:900px;margin:52px auto 0;row-gap:60px}
.class-item{display:flex;gap:18px}
.hex{width:84px;height:96px;flex:none}
.class-item h4{font-size:17px;font-weight:700;color:#333;text-transform:uppercase;line-height:1.25;width:300px}
.class-item p{font-size:13px;color:var(--muted);line-height:1.5;margin-top:4px}
.read-more{color:var(--orange);font-size:13px}
.center{text-align:center}
.btn-outline{background:#ddd;color:#333;border:2px solid #bbb;font-size:14px}

/* descriptions */
.descriptions{position:relative;height:457px;background:linear-gradient(135deg,#1b4c58,#23606c 50%,#173f49);color:var(--white);padding-top:58px;text-align:center}
.badge-new{position:absolute;left:145px;top:30px;width:100px;height:100px;border-radius:50%;background:var(--magenta);border:6px solid var(--white);display:flex;align-items:center;justify-content:center;font-family:"Cabin",sans-serif;font-weight:700;font-size:22px}
.descriptions h2{font-size:38px;font-weight:600}
.descriptions .lead{font-style:italic;font-size:17px;margin-top:8px}
.desc-row{display:flex;justify-content:center;gap:60px;margin:50px 0 36px}
.desc-item{width:260px;font-size:14px;line-height:1.4}
.desc-item svg{display:block;margin:0 auto 12px}
.btn-light{background:var(--white);color:#333}

/* newsletter */
.newsletter{height:309px;background:var(--light);padding-top:62px}
.signup{display:flex;justify-content:center;gap:20px;margin-top:38px}
.field{height:40px;border:1px solid #ccc;background:var(--white);font-size:13px;color:#999;padding:11px 14px}
.signup .field{width:340px}
.signup .btn-outline{padding:10px 18px}

/* social */
.social{height:229px;display:flex;justify-content:center;align-items:center;gap:20px}
.social-box{width:100px;height:100px;border:3px solid;border-radius:4px;display:flex;align-items:center;justify-content:center}
.social-box span{width:34px;height:34px;border-radius:50%;background:currentColor}

/* contact */
.contact{height:782px;background:var(--dark);color:var(--white);padding:70px 137px 0}
.contact .lead{font-style:italic;font-size:17px;text-align:center;margin-top:8px}
.contact-body{display:flex;gap:40px;margin-top:20px}
.enquiry{width:443px}
.enquiry h3{font-size:32px;margin-bottom:14px}
.enquiry .field{width:100%;margin-bottom:16px;border-radius:3px;border:none}
.enquiry textarea.field{height:150px;resize:none;font-family:inherit;display:block}
.submit{background:var(--white);color:#333;padding:10px 16px;font-size:14px}
.map{width:440px;height:335px;margin-top:48px;background:linear-gradient(135deg,#e8e4da,#d5d1c8);border:6px solid var(--white)}
.contact-info{display:flex;justify-content:space-between;margin-top:50px}
.info{display:flex;gap:12px}
.info strong{color:var(--cyan);display:block;font-size:17px}
.info p{font-size:14px;line-height:1.4}

/* footer */
.site-footer{height:66px;display:flex;align-items:center;justify-content:space-between;padding:0 137px;font-size:13px;color:var(--muted)}
.site-footer nav{display:flex;gap:24px}
</style>
</head>
<body>

<header class="site-header">
  <div class="brand">Taro Velmund</div>
  <nav class="main-nav">
    <span class="active">Home</span><span>About Us</span><span>Our Services</span><span>Education</span><span>Contact Us</span>
    <div class="account"><span class="login">Login</span><span class="register">Register</span></div>
  </nav>
</header>

<section class="hero">
  <div role="img" aria-label="Therapist treating a patient's leg in a clinic" style="position:absolute;inset:0"></div>
  <div class="hero-arrow prev"><svg viewBox="0 0 52 52"><path d="M30 16 20 26l10 10" fill="none" stroke="#fff" stroke-width="4"/></svg></div>
  <div class="hero-arrow next"><svg viewBox="0 0 52 52"><path d="M22 16l10 10-10 10" fill="none" stroke="#fff" stroke-width="4"/></svg></div>
  <div class="hero-caption">
    <h1>Welcome to Taro Velmund</h1>
    <p>We firmly believe that you know your body better than anyone else and everything we do springs</p>
  </div>
</section>

<section class="about">
  <h2 class="section-title">Who we are</h2>
  <p class="section-sub">We firmly believe that you know your body better than anyone else</p>
  <div class="divider"></div>
  <p>We firmly believe that you know your body better than anyone else and everything we do springs from that philosophy. We meld our expertise and experience with your insight to uncover the best route for your physical well-being.</p>
</section>

<section class="split">
  <div class="split-panel practice">
    <h3>Private Practice</h3>
    <p>We offer a gentle blend of movement, education and therapeutic care for a wide variety of patients and clients, from sports therapy and manual therapy to athletic management and rehabilitation.</p>
    <span class="btn">View more information</span>
  </div>
  <div class="split-panel education">
    <h3>Education</h3>
    <p>We provide advanced continuing education to manual practitioners. Taro Velmund teaches clinically tested, effective manual techniques in a way that students can immediately put to use in their practice.</p>
    <span class="btn">Register for classes</span>
  </div>
</section>

<section class="next-class">
  <h2 class="section-title">Next Class</h2>
  <p class="section-sub">Evaluation and Manual Treatment of the Pelvis, Sacrum &amp; Lumbar Spine</p>
  <div class="divider"></div>
  <p class="next-date">September 19-21 Sacramento, CA</p>
  <div class="class-grid">
    <div class="class-item">
      <svg class="hex" viewBox="0 0 84 96"><path d="M42 0l42 24v48L42 96 0 72V24z" fill="#2f2b52"/><text x="42" y="44" fill="#f0a030" font-family="Cabin" font-weight="700" font-size="22" text-anchor="middle">7-9</text><text x="42" y="66" fill="#fff" font-family="Cabin" font-weight="700" font-size="16" text-anchor="middle">FEB</text></svg>
      <div><h4>Evaluation and Manual Treatment of the Respiratory System</h4><p>Sacramento, CA<br>Taro Velmund, ATC, MT, SP, CAMTC<br><span class="read-more">[Read More...]</span></p></div>
    </div>
    <div class="class-item">
      <svg class="hex" viewBox="0 0 84 96"><path d="M42 0l42 24v48L42 96 0 72V24z" fill="#2f2b52"/><text x="42" y="44" fill="#f0a030" font-family="Cabin" font-weight="700" font-size="22" text-anchor="middle">11-13</text><text x="42" y="66" fill="#fff" font-family="Cabin" font-weight="700" font-size="16" text-anchor="middle">APR</text></svg>
      <div><h4>Evaluation and Manual Treatment of the Talus, Pubes and S/C Joint</h4><p>Sacramento, CA<br>Taro Velmund, ATC, MT, SP, CAMTC<br><span class="read-more">[Read More...]</span></p></div>
    </div>
    <div class="class-item">
      <svg class="hex" viewBox="0 0 84 96"><path d="M42 0l42 24v48L42 96 0 72V24z" fill="#2f2b52"/><text x="42" y="44" fill="#f0a030" font-family="Cabin" font-weight="700" font-size="22" text-anchor="middle">14-16</text><text x="42" y="66" fill="#fff" font-family="Cabin" font-weight="700" font-size="16" text-anchor="middle">MAR</text></svg>
      <div><h4>Rendale's Neurovascular Concepts for the Manual Practitioner</h4><p>Sacramento, CA<br>Taro Velmund, ATC, MT, SP, CAMTC<br><span class="read-more">[Read More...]</span></p></div>
    </div>
    <div class="class-item">
      <svg class="hex" viewBox="0 0 84 96"><path d="M42 0l42 24v48L42 96 0 72V24z" fill="#2f2b52"/><text x="42" y="44" fill="#f0a030" font-family="Cabin" font-weight="700" font-size="22" text-anchor="middle">16-18</text><text x="42" y="66" fill="#fff" font-family="Cabin" font-weight="700" font-size="16" text-anchor="middle">APR</text></svg>
      <div><h4>Evaluation and Manual Treatment of the Pediatric Patient</h4><p>Sacramento, CA<br>Taro Velmund, ATC, MT, SP, CAMTC and Owen Harlow, PT<br><span class="read-more">[Read More...]</span></p></div>
    </div>
  </div>
  <p class="center" style="margin-top:64px"><span class="btn btn-outline">View all upcoming class schedule</span></p>
</section>

<section class="descriptions" role="img" aria-label="Classroom of students practising manual therapy, tinted teal">
  <div class="badge-new">NEW</div>
  <h2>Class Descriptions 2014</h2>
  <p class="lead">The 2014 class schedule is posted on the Doltra Foundation's website.</p>
  <div class="divider" style="background:rgba(255,255,255,.4)"></div>
  <div class="desc-row">
    <div class="desc-item"><svg width="30" height="30" viewBox="0 0 30 30"><path d="M6 24l3-8L21 4l5 5-12 12z" fill="#fff"/></svg>Evaluation and Manual Treatment of the Respiratory System<br><span class="read-more">[Read More...]</span></div>
    <div class="desc-item"><svg width="30" height="30" viewBox="0 0 30 30"><path d="M6 24l3-8L21 4l5 5-12 12z" fill="#fff"/></svg>Rendale's Neurovascular Concepts for the Manual Practitioner<br><span class="read-more">[Read More...]</span></div>
    <div class="desc-item"><svg width="30" height="30" viewBox="0 0 30 30"><path d="M6 24l3-8L21 4l5 5-12 12z" fill="#fff"/></svg>Evaluation and Manual Treatment of the Talus, Pubes and S/C Joint<br><span class="read-more">[Read More...]</span></div>
  </div>
  <span class="btn btn-light">View all classes</span>
</section>

<section class="newsletter">
  <h2 class="section-title">Newsletter Signup</h2>
  <p class="section-sub">Sign up for our mailing list and we'll keep you updated!</p>
  <div class="divider"></div>
  <div class="signup">
    <div class="field">Enter Your Name</div>
    <div class="field">Enter Your Email Address</div>
    <span class="btn btn-outline">Subscribe!</span>
  </div>
</section>

<section class="social" aria-label="Social networks">
  <div class="social-box" style="color:#3b5a9a"><span></span></div>
  <div class="social-box" style="color:#2aa9e0"><span></span></div>
  <div class="social-box" style="color:#d8432f"><span></span></div>
  <div class="social-box" style="color:#1f7bb6"><span></span></div>
  <div class="social-box" style="color:#f39a1e"><span></span></div>
</section>

<section class="contact">
  <h2 class="section-title" style="color:#fff">Contact</h2>
  <p class="lead">Come on. We have introduced ourself much. Just leave a message.</p>
  <div class="divider" style="background:#666"></div>
  <div class="contact-body">
    <div class="enquiry">
      <h3>Enquiry</h3>
      <div class="field">Name</div>
      <div class="field">Email Address</div>
      <div class="field">Subject</div>
      <textarea class="field" placeholder="Message"></textarea>
      <span class="btn submit" style="margin-top:16px">Submit</span>
    </div>
    <div class="map" role="img" aria-label="Street map showing the clinic location"></div>
  </div>
  <div class="contact-info">
    <div class="info"><svg width="26" height="34" viewBox="0 0 26 34"><path d="M13 0a13 13 0 0113 13c0 9-13 21-13 21S0 22 0 13A13 13 0 0113 0z" fill="#fff"/><circle cx="13" cy="13" r="5" fill="#3b3b3b"/></svg><p><strong>Location :</strong>4470 Marrow Lane<br>Sacramento, CA 95811</p></div>
    <div class="info"><svg width="24" height="34" viewBox="0 0 24 34"><rect x="2" y="0" width="20" height="34" rx="3" fill="#fff"/><rect x="5" y="4" width="14" height="22" fill="#3b3b3b"/></svg><p><strong>Phone :</strong>(555) 014-2287</p></div>
    <div class="info"><svg width="34" height="24" viewBox="0 0 34 24"><rect width="34" height="24" rx="2" fill="#fff"/><path d="M1 2l16 12L33 2" fill="none" stroke="#3b3b3b" stroke-width="2"/></svg><p><strong>Email :</strong>Contact@TaroVelmund.com</p></div>
  </div>
</section>

<footer class="site-footer">
  <span>Copyright © 2014 Taro Velmund. All Rights Reserved</span>
  <nav><span>Home</span><span>About Us</span><span>Our Services</span><span>Education</span><span>Contact Us</span></nav>
</footer>

</body>
</html>
```